Harbor Vantage needs new design business card

We are video surveillance and analytics software development company.
I am looking for a professional business card.
Our website is www.harborvantage-example.com.au
Please have a loo and get the feel for who we are and what we do.
I do not know what else to give you apart from good luck and I hope your design gets selected.
Thank you very much for participating
Industry/Entity Type
Business
Contact Information for Business Card
Address
27/14 Pemberly Street Millbrook NSW 2199
Telephone 1300 582 741
Mobile 0450 713 258
email: marcus@harborvantage-example.com.au
name
Marcus Felder
Position
Managing Director
Font styles to use
Other font styles liked:
- Arial
Look and feel

```html
<!DOCTYPE html>
<html lang="en">
<head>
<meta charset="utf-8">
<title>Harbor Vantage – Business Card</title>
<link rel="stylesheet" href="https://fonts.googleapis.com/css2?family=Montserrat:wght@400;500;700&display=swap">
<style>
  :root {
    --navy: #1c3563;
    --navy-light: #2e4a80;
    --slate: #6b7f98;
    --ink: #2a2f38;
    --paper: #ffffff;
    --backdrop: #e2e2e2;
  }
  * { box-sizing: border-box; margin: 0; padding: 0; }
  html, body {
    width: 1200px; height: 852px; overflow: hidden;
    background: var(--backdrop);
    font-family: "Montserrat", Arial, sans-serif;
  }
  .sheet {
    width: 1200px; height: 852px;
    display: flex; flex-direction: column;
    align-items: center; justify-content: center; gap: 50px;
  }
  .card {
    position: relative;
    width: 620px; height: 354px;
    background: var(--paper);
    border-radius: 16px;
    overflow: hidden;
    box-shadow: 0 4px 14px rgba(0,0,0,.18);
  }
  /* Front */
  .card--front {
    display: flex; align-items: center; justify-content: center; gap: 16px;
  }
  .brand-mark {
    width: 34px; height: 34px; border-radius: 50%;
    background: var(--navy);
  }
  .brand-name {
    font-weight: 700; font-size: 40px; letter-spacing: 1px;
    color: var(--navy); text-transform: uppercase;
  }
  /* Back */
  .card__band { position: absolute; inset: 0; }
  .band-brand {
    position: absolute; left: 56px; top: 50%;
    transform: translate(-50%, -50%) rotate(90deg);
    transform-origin: center;
    left: 110px;
    font-weight: 700; font-size: 26px; letter-spacing: 1px;
    color: var(--paper); text-transform: uppercase; white-space: nowrap;
  }
  .details {
    position: absolute; left: 330px; top: 62px;
    color: var(--ink);
  }
  .person__name {
    font-weight: 700; font-size: 18px; letter-spacing: 2px;
    color: var(--navy); text-transform: uppercase;
  }
  .person__role { font-size: 11.5px; margin-top: 2px; }
  .address { font-size: 12.5px; line-height: 1.45; margin-top: 40px; }
  .contacts { list-style: none; margin-top: 22px; font-size: 12.5px; }
  .contacts li { display: flex; align-items: center; gap: 8px; line-height: 1.55; }
  .contacts svg { width: 11px; height: 11px; fill: var(--navy); flex: none; }
</style>
</head>
<body>
<main class="sheet">
  <section class="card card--front" aria-label="Card front">
    <span class="brand-mark"></span>
    <span class="brand-name">Harbor Vantage</span>
  </section>

  <section class="card card--back" aria-label="Card back">
    <svg class="card__band" viewBox="0 0 620 354" preserveAspectRatio="none" aria-hidden="true">
      <defs>
        <linearGradient id="bandShade" x1="0" x2="1">
          <stop offset="0" stop-color="var(--navy)"/>
          <stop offset="1" stop-color="var(--navy-light)"/>
        </linearGradient>
      </defs>
      <path d="M0,0 H196 C250,90 196,210 282,354 H0 Z" fill="var(--slate)"/>
      <path d="M0,0 H184 C238,90 184,210 268,354 H0 Z" fill="url(#bandShade)"/>
    </svg>
    <span class="band-brand">Harbor Vantage</span>

    <div class="details">
      <p class="person__name">Marcus Felder</p>
      <p class="person__role">Managing Director</p>
      <p class="address">27/14 Pemberly Street<br>Millbrook NSW 2199</p>
      <ul class="contacts">
        <li><svg viewBox="0 0 12 12"><path d="M1 4c0-2 2-3 5-3s5 1 5 3v1H8V4H4v1H1zM2 6h8l1 5H1z"/></svg>1300 582 741</li>
        <li><svg viewBox="0 0 12 12"><rect x="3" y="0" width="6" height="12" rx="1"/></svg>0450 713 258</li>
        <li><svg viewBox="0 0 12 12"><path d="M0 2h12v8H0zM0 2l6 5 6-5"/></svg>marcus@harborvantage-example.com.au</li>
        <li><svg viewBox="0 0 12 12"><circle cx="6" cy="6" r="6"/></svg>www.harborvantage-example.com.au</li>
      </ul>
    </div>
  </section>
</main>
</body>
</html>
```